Investment Group needs a web page design

We need a web page design for a San Francisco-based investment group called 'Talvirow LLC'. The final design should be stylish and attractive to the idea while retaining a sense of stability and professionalism. A great example is http://brambleharborgroup.com/.

I am attaching the group's logo which should be the base for the webpage design.
Updates

Please note that I am interested in a single webpage that presents basic information. See the following example: http://brambleharborgroup.com/

Target Market(s)

persons doing initial due diligence and trying to assess what kind of group we are.

Industry/Entity Type

Investment

Font styles to use
Serif

Colors
86acd3
3176b5
0355a3

Requirements
Nice to have
• Would love the design to incorporate the concept - 'Sen no Sen: a block and counter attack while the opponent is attacking.'
Should not have
• Do not include trite illustrations related to finance, money or investing.

```html
<!DOCTYPE html>
<html lang="en">
<head>
<meta charset="utf-8">
<title>Talvirow LLC</title>
<link href="https://fonts.googleapis.com/css2?family=Oswald:wght@400;500&family=Quicksand:wght@300;400;500&display=swap" rel="stylesheet">
<style>
  :root {
    --navy-deep: #03101f;
    --navy: #062a4d;
    --blue: #0355a3;
    --blue-mid: #3176b5;
    --blue-soft: #86acd3;
    --cyan-glow: #5fe3f5;
    --heading-blue: #1c7cc0;
    --card-white: #ffffff;
    --text-grey: #8a8f94;
    --rule-grey: #e3e6e9;
    --ink: #111111;
    --footer-rule: rgba(255,255,255,0.55);
  }
  * { margin: 0; padding: 0; box-sizing: border-box; }
  html, body {
    width: 1200px;
    height: 583px;
    overflow: hidden;
    background: var(--navy-deep);
  }
  .page {
    position: relative;
    width: 1200px;
    height: 583px;
    overflow: hidden;
    font-family: "Quicksand", sans-serif;
  }
  .hero-backdrop {
    position: absolute;
    inset: 0;
    background:
      radial-gradient(ellipse 90px 60px at 690px 285px, rgba(210,255,255,0.95), rgba(95,227,245,0) 100%),
      radial-gradient(ellipse 300px 170px at 680px 290px, rgba(95,227,245,0.55), rgba(95,227,245,0) 100%),
      radial-gradient(ellipse 420px 260px at 1010px 190px, rgba(134,172,211,0.45), rgba(134,172,211,0) 100%),
      radial-gradient(ellipse 360px 300px at 170px 260px, rgba(49,118,181,0.55), rgba(49,118,181,0) 100%),
      linear-gradient(180deg, #0a4f8c 0%, var(--blue) 30%, var(--navy) 65%, var(--navy-deep) 100%);
  }
  .brand {
    position: absolute;
    left: 394px;
    top: 0;
    width: 421px;
    height: 122px;
    background: var(--card-white);
    box-shadow: 3px 4px 8px rgba(0,0,0,0.45);
    display: flex;
    align-items: center;
    gap: 13px;
    padding: 18px 0 0 27px;
  }
  .brand-mark {
    width: 55px;
    height: 55px;
    background: var(--ink);
  }
  .brand-name {
    font-family: "Quicksand", sans-serif;
    font-weight: 500;
    font-size: 56px;
    letter-spacing: 1px;
    color: var(--ink);
    line-height: 1;
  }
  .welcome {
    position: absolute;
    top: 230px;
    left: 0;
    width: 100%;
    text-align: center;
    font-family: "Quicksand", sans-serif;
    font-weight: 300;
    font-size: 44px;
    color: #ffffff;
    letter-spacing: 0.5px;
  }
  .info-cards {
    position: absolute;
    top: 412px;
    left: 179px;
    display: flex;
    gap: 15px;
  }
  .info-card {
    width: 271px;
    height: 100px;
    background: var(--card-white);
    box-shadow: 2px 3px 6px rgba(0,0,0,0.4);
    padding: 9px 9px 0 9px;
  }
  .info-card h2 {
    font-family: "Oswald", sans-serif;
    font-weight: 500;
    font-size: 14px;
    color: var(--heading-blue);
    text-transform: uppercase;
    letter-spacing: 0.3px;
    padding-bottom: 2px;
    border-bottom: 1px solid var(--rule-grey);
  }
  .info-card p {
    font-size: 12px;
    line-height: 15px;
    color: var(--text-grey);
    margin-top: 9px;
    letter-spacing: 0.2px;
  }
  .info-card p.indented { padding-left: 6px; }
  .site-footer {
    position: absolute;
    top: 554px;
    left: 179px;
    width: 843px;
    border-top: 1px solid var(--footer-rule);
    text-align: center;
    padding-top: 8px;
    font-size: 12px;
    color: #ffffff;
    letter-spacing: 0.3px;
  }
</style>
</head>
<body>
  <main class="page">
    <div class="hero-backdrop" role="img" aria-label="Close-up photograph of a pen tip over a glowing blue line chart"></div>

    <header class="brand">
      <span class="brand-mark"></span>
      <span class="brand-name">TALVIROW</span>
    </header>

    <h1 class="welcome">Welcome to Talvirow LLC.</h1>

    <section class="info-cards">
      <article class="info-card">
        <h2>Talvirow LLC.</h2>
        <p>Lorem ipsum dolor sit amet, consectetur adipisicing elit, sed do eiusmod tempor incididunt ut labore.</p>
      </article>
      <article class="info-card">
        <h2>Location</h2>
        <p class="indented">Complete Location Here.<br>Complete Adress Here.</p>
      </article>
      <article class="info-card">
        <h2>Contact</h2>
        <p class="indented">Phone: 123.456.7890<br>Email: contact@talvirow.com</p>
      </article>
    </section>

    <footer class="site-footer">© 2014 Talvirow LLC. All Rights Reserved.</footer>
  </main>
</body>
</html>
```